Affiliate website design and wireframe

We need a design of an affiliate website for an application we purchased, it is important that you build the website pages according to the developer of the applications specifications (please see attached documents) the developer of the application will configure the pages and add them to the site. Please take special note of his comments below.

We all so need you to create a wire frame so the developer can test everything (http://sketchwire.tolvaro.vn/)

It will be the homepage and about 16 inner pages (please see attached files)
Here is our website http://bluvendmarket.com/affiliate/affiliates/index.php

The version of the software we purchased is the Kivo Partner Hubline version

Comments from the developers

1. I will need the source files of the design (photoshop .psd files and font files if custom fonts are used), since the implementation is closely bound to component sizes (like border width, margin width etc.) and colors. If you own a corporate design manual, it's crucial to send it as well. Also, please, make sure if you use custom fonts, that these allow legal website integration (like google web fonts).

2. Any and every content is controlled via templates. All editing/adding/removing etc. is done here. The template files are essentially html/php documents, they use a template engine called quillo (http://www.quillo.net/) which has it's own language similar to php.

3. .psd files are ideal, because we deal with the specifics of KPX/KPH implementation on a daily basis. Any html/css developed in advance may prove to be a poor choice. You may choose to let an in-house developer do the job, but experience wise this is more costly, since he will not be accustomed to the template/functionality systems of KPX/KPH.

4. I will need the source files of the design (photoshop .psd files and font files if custom fonts are used), since the implementation is closely bound to component sizes (like border width, margin width etc.) and colors. If you own a corporate design manual, it's crucial to send it as well. Also, please, make sure if you use custom fonts, that these allow legal website integration (like google web fonts).

Regards,

Dorek Hanval
Multimedia Design

We prefer illustrations more than pictures of real people.

This is the home page, it is asking for Merchant and Affiliate sign up, not just affiliate.

http://bluvendmarket.com/affiliate/index.php

Please note the home page features both Merchant and Affiliate sign up

We are looking for illustration design not just stock images

Please remember the search menu that searches for the available programs, see the example we gave you, look at the search menu at the top of the page http://www.tradelumo.com/

We are reviewing everything, no need to send more designs

Target Market(s)

Natural Products Manufacturers
Natural products Sales reps
Natural Products Bloggers
Social Marketing

Industry/Entity Type

Software

Requirements
Must have
• 1. All links on pages should go to the appropriate pages.
2. Colors can be based on our logo design (look at the attachments)
3. Here is our website http://bluvendmarket.com/affiliate/affiliates/index.php
4. We have attached a drawing of how we think the homepage concept should follow.
5. Main concept of design, is trying to show our sales people (Affiliates) are doing multiple things to advertise and sell the merchants products.(see logo)
6. Need to be able to edit all text and images.
7. Our target audience is Natural product sales people (Advertisers, bloggers, ext) and natural product manufacturers.
8. You can speak to the company who made the application, through live chat, on there website http://www.kivopartnerhubline.com/
Nice to have
• See Attached Documents.
site should take up whole website pages
Look For fun Illustrated Website, one of the better ones we have seen is http://www.tradelumo.com/index.cfm
Should not have
• Please look very carefully at developers comment above.

```html
<!DOCTYPE html>
<html lang="en">
<head>
<meta charset="utf-8">
<title>Bluvend Market — Affiliate Home</title>
<link href="https://fonts.googleapis.com/css2?family=Roboto:wght@300;400;500;700&display=swap" rel="stylesheet">
<style>
:root{
  --navy:#173f73;
  --navy-dark:#0f2f5a;
  --card-top:#2461ad;
  --card-bottom:#163f7a;
  --green:#6fa516;
  --green-light:#8cc63f;
  --green-btn:#79b51f;
  --grey-bg:#e6e6e8;
  --grey-hero-top:#e3e3e3;
  --grey-hero-bottom:#b9b9b9;
  --floor:#6d6d6d;
  --text:#444;
  --text-soft:#777;
  --white:#fff;
  --footer-top:#2a2522;
  --footer-bottom:#000;
  --link-blue:#2461ad;
}
*{box-sizing:border-box;margin:0;padding:0}
html,body{width:1200px;height:2466px;overflow:hidden}
body{font-family:'Roboto',Arial,sans-serif;color:var(--text);background:var(--white);position:relative}
.abs{position:absolute}

/* header */
.site-header{position:absolute;left:0;top:0;width:1200px;height:135px}
.top-strip{height:79px;background:var(--white)}
.nav-bar{position:absolute;top:79px;left:0;width:1200px;height:56px;background:var(--navy)}
.brand{position:absolute;left:169px;top:0;width:286px;height:138px;background:var(--white);display:flex;align-items:flex-end;justify-content:center;gap:10px;padding-bottom:26px}
.brand-dot{width:22px;height:22px;border-radius:50%;background:var(--green)}
.brand-name{font-weight:700;font-size:25px;color:var(--green);letter-spacing:.5px}
.login-btns{position:absolute;right:181px;top:11px;display:flex;gap:8px}
.login-btns span{font-size:10px;font-weight:700;color:var(--white);padding:3px 8px;text-transform:uppercase}
.btn-aff{background:var(--navy)}
.btn-mer{background:var(--green-btn)}
.top-links{position:absolute;right:181px;top:48px;display:flex;gap:26px;font-size:11px;font-weight:700;color:#555;text-transform:uppercase}
.main-nav{position:absolute;left:480px;top:93px;display:flex;gap:28px}
.main-nav li{list-style:none;color:var(--white);font-weight:700;font-size:13px;text-transform:uppercase;line-height:13px}
.main-nav small{display:block;font-weight:400;font-size:8px;text-transform:none;margin-top:2px}

/* hero */
.hero{position:absolute;top:135px;left:0;width:1200px;height:329px;background:linear-gradient(var(--grey-hero-top),var(--grey-hero-bottom) 78%,var(--floor) 79%,#5a5a5a)}
.hero-tabs{position:absolute;left:184px;top:90px;display:flex;gap:10px}
.hero-tabs span{font-size:12px;color:var(--white);padding:7px 24px}
.tab-aff{background:var(--green-btn)}
.tab-mer{background:var(--navy)}
.hero-title{position:absolute;left:183px;top:142px;font-weight:300;font-size:40px;line-height:38px;color:var(--white)}
.btn-start{position:absolute;left:184px;top:250px;background:var(--green-btn);color:var(--white);font-size:12px;padding:7px 26px;text-transform:uppercase}
.hero-art{position:absolute;left:543px;top:18px;width:460px;height:311px;border-radius:4px;background:linear-gradient(#c9cfd6,#8a96a5 60%,#3f5b7a)}

/* affiliates / merchants */
.audiences{position:absolute;top:464px;left:0;width:1200px;height:393px;background:linear-gradient(var(--green),var(--green-light))}
.pointer{position:absolute;left:0;top:857px;width:1200px;height:40px}
.audience{position:absolute;top:0;width:400px;text-align:center;color:var(--white)}
.audience h2{font-weight:300;font-size:34px;margin-top:26px}
.badge{width:92px;height:92px;border-radius:50%;background:var(--white);margin:22px auto 0;display:flex;align-items:center;justify-content:center;box-shadow:0 0 0 4px rgba(255,255,255,.5)}
.feature-list{display:flex;justify-content:center;gap:40px;margin-top:38px;font-size:13px;text-align:left}
.feature-list li{list-style:none;line-height:22px;display:flex;align-items:center;gap:6px}
.feature-list .dots{display:inline-block;border-bottom:2px dotted var(--white);width:32px;height:1px;margin-top:3px}
.feature-list i{display:inline-block;width:11px;height:11px;border-radius:2px;background:var(--white)}
.learn{display:inline-flex;align-items:center;gap:8px;margin-top:26px;background:var(--white);color:#444;font-size:12px;padding:7px 16px;border-radius:3px}
.learn b{width:14px;height:8px;border-radius:50%;background:#444}

/* channels */
.channels{position:absolute;top:857px;left:0;width:1200px;height:623px}
.section-title{position:absolute;left:0;width:1200px;text-align:center;font-weight:300;font-size:33px;color:#555}
.card{position:absolute;width:250px;height:165px;background:linear-gradient(var(--card-top),var(--card-bottom));color:var(--white);text-align:center;padding-top:86px}
.card .seal{position:absolute;left:81px;top:-24px;width:88px;height:88px;border-radius:50%;background:var(--white);border:3px dashed #d5d9e2;display:flex;align-items:center;justify-content:center}
.card h3{font-size:13px;font-weight:700;text-transform:uppercase;letter-spacing:.3px}
.card p{font-size:10px;line-height:14px;margin:8px 24px 0;opacity:.9}

/* testimonials */
.love{position:absolute;top:1480px;left:0;width:1200px;height:529px;background:var(--grey-bg)}
.quote-card{position:absolute;left:197px;top:103px;width:395px;height:350px;background:var(--white);border:1px solid #d8d8d8;padding:18px 20px;font-size:11px;line-height:17px;color:#555}
.quote-mark{font-size:40px;font-weight:700;color:#555;line-height:30px}
.avatar{float:right;width:66px;height:74px;margin:0 0 6px 10px;background:linear-gradient(#dfe3e8,#9aa3ad)}
.quote-card p{margin-bottom:12px}
.quote-card a{color:var(--link-blue);font-weight:700;text-decoration:underline}
.author{font-size:15px;font-weight:700;color:var(--link-blue);margin-top:10px}
.role{font-size:11px;color:#555}
.big-quote{position:absolute;right:20px;bottom:-18px;font-size:150px;font-weight:700;color:#e6e6e6;line-height:150px}
.partner{position:absolute;background:var(--white);border:1px solid #d8d8d8;display:flex;align-items:center;justify-content:center}
.partner span{display:block;border-radius:6px;background:#c9ced6}
.dots-nav{position:absolute;left:0;width:1200px;top:477px;display:flex;justify-content:center;gap:8px}
.dots-nav i{width:10px;height:10px;border-radius:50%;background:#999}
.dots-nav i:first-child{background:var(--link-blue)}

/* footer */
.site-footer{position:absolute;top:2009px;left:0;width:1200px;height:457px;background:linear-gradient(var(--footer-top),var(--footer-bottom));color:#ccc}
.foot-h{position:absolute;font-size:16px;color:var(--white);padding-bottom:10px;border-bottom:1px solid #555}
.about-text{position:absolute;left:186px;top:71px;width:490px;font-size:8.5px;line-height:17px;color:#ddd}
.foot-col{position:absolute;top:270px;font-size:10px;line-height:17px;color:#777;list-style:none}
.phone{position:absolute;left:722px;top:71px;font-size:22px;color:var(--white)}
.email{position:absolute;left:722px;top:101px;font-size:15px;color:var(--white)}
.bubble{position:absolute;left:716px;top:137px;width:252px;height:106px;background:#4a4a4a;padding:14px 12px;font-size:11px;line-height:16px;color:#eee}
.bubble p{margin-bottom:14px}
.bubble:after{content:"";position:absolute;left:18px;bottom:-20px;border-left:0 solid transparent;border-right:20px solid transparent;border-top:20px solid #4a4a4a}
.social{position:absolute;left:718px;top:318px;display:flex;gap:12px}
.social i{width:50px;height:50px;border-radius:50%;background:#6b6b6b;border:2px dashed #999}
.foot-brand{position:absolute;left:184px;top:398px;display:flex;align-items:center;gap:6px;font-size:13px;font-weight:700;color:var(--white)}
.foot-brand b{width:12px;height:12px;border-radius:50%;background:var(--white)}
.copy{position:absolute;left:776px;top:406px;font-size:9px;color:var(--white)}
</style>
</head>
<body>

<header class="site-header">
  <div class="top-strip"></div>
  <div class="nav-bar"></div>
  <div class="brand"><span class="brand-dot"></span><span class="brand-name">BLUVEND MARKET</span></div>
  <div class="login-btns"><span class="btn-aff">Affiliate Login</span><span class="btn-mer">Merchant Login</span></div>
  <nav class="top-links"><span>What is Affiliate Marketing?</span><span>Merchants Join Here</span><span>Affiliaate Sign Up</span></nav>
  <ul class="main-nav">
    <li>Popular<small>Merchants</small></li>
    <li>Home&amp;Garden<small>Merchants</small></li>
    <li>Fashion<small>Merchants</small></li>
    <li>Green<small>Merchants</small></li>
    <li>Business<small>Merchants</small></li>
    <li>More<small>Merchants</small></li>
  </ul>
</header>

<section class="hero">
  <div class="hero-tabs"><span class="tab-aff">Affiliates Signup</span><span class="tab-mer">Merchants Signup</span></div>
  <h1 class="hero-title">Make Money<br>Make Sense.</h1>
  <span class="btn-start">Get Started</span>
  <div class="hero-art" role="img" aria-label="Illustration of a person at a desk working on a computer, with speech bubbles showing sale, shopping basket, dollar and card icons"></div>
</section>

<section class="audiences">
  <div class="audience" style="left:194px">
    <h2>Affiliates</h2>
    <div class="badge"><svg width="44" height="40" viewBox="0 0 44 40"><g fill="#555"><rect x="6" y="24" width="5" height="12"/><rect x="14" y="18" width="5" height="18"/><rect x="22" y="12" width="5" height="24"/><rect x="30" y="20" width="5" height="16"/></g><path d="M4 38H40M4 20L14 12 22 16 36 4" stroke="#555" stroke-width="2" fill="none"/></svg></div>
    <div class="feature-list">
      <ul><li>Automotive<span class="dots"></span><i></i></li><li>Business<span class="dots"></span><i></i></li><li>Careers<span class="dots"></span><i></i></li><li>Education<span class="dots"></span><i></i></li></ul>
      <ul><li>Clothing<span class="dots"></span><i></i></li><li>Auction<span class="dots"></span><i></i></li><li>Media<span class="dots"></span><i></i></li><li>Health<span class="dots"></span><i></i></li></ul>
    </div>
    <span class="learn"><b></b>Learn More</span>
  </div>
  <div class="audience" style="left:609px">
    <h2>Merchants</h2>
    <div class="badge"><svg width="44" height="40" viewBox="0 0 44 40"><g fill="#555"><rect x="6" y="14" width="4" height="22"/><rect x="12" y="8" width="4" height="28"/><rect x="18" y="14" width="4" height="22"/></g><circle cx="28" cy="20" r="8" fill="none" stroke="#555" stroke-width="3"/><path d="M33 26L40 34M4 38H40" stroke="#555" stroke-width="3"/></svg></div>
    <div class="feature-list">
      <ul style="text-align:right"><li>Affiliate Diagnostics<span class="dots"></span><i></i></li><li>Merchant Recommendations<span class="dots"></span><i></i></li><li>Continuing Education<span class="dots"></span><i></i></li><li>Training Webinars<span class="dots"></span><i></i></li></ul>
    </div>
    <span class="learn"><b></b>Learn More</span>
  </div>
</section>
<svg class="pointer" viewBox="0 0 1200 40"><polygon points="560,0 640,0 600,39" fill="#8cc63f"/></svg>

<section class="channels">
  <h2 class="section-title" style="top:68px">We Leave the Marketing Decisions to You</h2>
  <div class="card" style="left:197px;top:164px"><span class="seal"><svg width="36" height="36" viewBox="0 0 36 36" fill="#1f4f8f"><circle cx="26" cy="8" r="5"/><circle cx="26" cy="28" r="5"/><circle cx="9" cy="18" r="5"/><path d="M9 18L26 8M9 18L26 28" stroke="#1f4f8f" stroke-width="3"/></svg></span><h3>Social Networks</h3><p>Lorem Ipsum is simply dummy text of the printing and typesetting industry.</p></div>
  <div class="card" style="left:475px;top:164px"><span class="seal"><svg width="36" height="36" viewBox="0 0 36 36"><rect x="11" y="6" width="14" height="26" rx="3" fill="none" stroke="#1f4f8f" stroke-width="3" transform="rotate(-20 18 18)"/></svg></span><h3>Phone Calls</h3><p>Lorem Ipsum is simply dummy text of the printing and typesetting industry.</p></div>
  <div class="card" style="left:755px;top:164px"><span class="seal"><svg width="36" height="36" viewBox="0 0 36 36" fill="none" stroke="#1f4f8f" stroke-width="2.5"><rect x="6" y="10" width="18" height="22"/><rect x="12" y="4" width="18" height="22" fill="#fff"/><path d="M16 11H26M16 16H26M16 21H24"/></svg></span><h3>Text Messages</h3><p>Lorem Ipsum is simply dummy text of the printing and typesetting industry.</p></div>
  <div class="card" style="left:197px;top:379px"><span class="seal"><svg width="38" height="30" viewBox="0 0 38 30" fill="none" stroke="#1f4f8f" stroke-width="3"><rect x="2" y="2" width="34" height="26"/><path d="M2 2L19 17 36 2M2 28L14 14M36 28L24 14"/></svg></span><h3>Email</h3><p>Lorem Ipsum is simply dummy text of the printing and typesetting industry.</p></div>
  <div class="card" style="left:475px;top:379px"><span class="seal"><svg width="36" height="36" viewBox="0 0 36 36" fill="none" stroke="#1f4f8f" stroke-width="3"><rect x="4" y="6" width="26" height="26"/><path d="M10 18L17 25 33 6"/></svg></span><h3>Banner Ads</h3><p>Lorem Ipsum is simply dummy text of the printing and typesetting industry.</p></div>
  <div class="card" style="left:755px;top:379px"><span class="seal"><svg width="36" height="36" viewBox="0 0 36 36" fill="none" stroke="#1f4f8f" stroke-width="3"><path d="M8 32L14 16 24 10 26 12 20 22 8 32ZM8 32L17 19"/><path d="M22 4A10 10 0 0 1 32 14M22 8A6 6 0 0 1 28 14"/></svg></span><h3>Blogs</h3><p>Lorem Ipsum is simply dummy text of the printing and typesetting industry.</p></div>
</section>

<section class="love">
  <h2 class="section-title" style="top:32px">Thousands of Online Business Love us!</h2>
  <article class="quote-card">
    <div class="quote-mark">&ldquo;</div>
    <div class="avatar" role="img" aria-label="Portrait photo of the reviewer"></div>
    <p>Lorem Ipsum has been the industry's standard dummy text ever since the 1500s, when an unknown printer took a galley of type and scrambled it to make a type specimen book.</p>
    <p>Lorem Ipsum has been the industry's standard dummy text ever since the 1500s, when an unknown printer took a galley of type and scrambled it to make a type specimen book. It has survived not only five centuries, but also the leap into electronic typesetting, remaining essentially unchanged. It was popularised in the 1960s with the release of Letraset sheets containing Lorem Ipsum passages, and more recently with desktop publishing software like Aldus PageMaker including versions of Lorem Ipsum. <a>read more</a></p>
    <div class="author">Calder Voss</div>
    <div class="role">Product Manager, Tindale Systems</div>
    <div class="big-quote">&rdquo;</div>
  </article>
  <div class="partner" style="left:608px;top:103px;width:110px;height:64px"><span style="width:70px;height:28px"></span></div>
  <div class="partner" style="left:733px;top:103px;width:143px;height:64px"><span style="width:100px;height:28px"></span></div>
  <div class="partner" style="left:891px;top:103px;width:128px;height:64px"><span style="width:50px;height:40px;border-radius:50%"></span></div>
  <div class="partner" style="left:608px;top:182px;width:110px;height:64px"><span style="width:70px;height:30px"></span></div>
  <div class="partner" style="left:733px;top:182px;width:207px;height:64px"><span style="width:160px;height:30px"></span></div>
  <div class="partner" style="left:955px;top:182px;width:64px;height:64px"><span style="width:36px;height:36px;border-radius:50%"></span></div>
  <div class="partner" style="left:608px;top:263px;width:110px;height:65px"><span style="width:64px;height:40px"></span></div>
  <div class="partner" style="left:733px;top:263px;width:207px;height:65px"><span style="width:170px;height:34px"></span></div>
  <div class="partner" style="left:955px;top:263px;width:64px;height:65px"><span style="width:36px;height:36px;border-radius:50%"></span></div>
  <div class="partner" style="left:608px;top:342px;width:110px;height:111px"><span style="width:60px;height:70px"></span></div>
  <div class="partner" style="left:733px;top:342px;width:286px;height:111px"><span style="width:230px;height:70px"></span></div>
  <div class="dots-nav"><i></i><i></i><i></i></div>
</section>

<footer class="site-footer">
  <h4 class="foot-h" style="left:186px;top:25px;width:490px">About Us</h4>
  <p class="about-text">Lorem Ipsum is simply dummy text of the printing and typesetting industry. Lorem Ipsum has been the industry's standard dummy text ever since the 1500s, when an unknown printer took a galley of type and scrambled it to make a type specimen book. It has survived not only five centuries, but also the leap into electronic typesetting, remaining essentially unchanged. It was popularised in the 1960s with the release of Letraset sheets containing Lorem Ipsum passages, and more recently with desktop publishing software like Aldus PageMaker including versions of Lorem Ipsum.</p>
  <h4 class="foot-h" style="left:186px;top:225px;width:136px">Get Started</h4>
  <h4 class="foot-h" style="left:338px;top:225px;width:136px">Help</h4>
  <h4 class="foot-h" style="left:492px;top:225px;width:184px">Company</h4>
  <ul class="foot-col" style="left:186px"><li>How it Works</li><li>Our Pricing</li><li>Why Us?</li></ul>
  <ul class="foot-col" style="left:338px"><li>FAQ's</li><li>Packing Tips</li><li>Contact us</li></ul>
  <ul class="foot-col" style="left:492px"><li>About Us</li><li>Services</li><li>Blog Posts</li></ul>
  <h4 class="foot-h" style="left:722px;top:25px;width:298px">Get in Touch</h4>
  <div class="phone">0000 000 0000</div>
  <div class="email">help@bluvendmarket.com</div>
  <div class="bubble"><p>Lorem Ipsum is simply dummy text of the printing and typesetting industry.</p><p>Lorem Ipsum is simply dummy text of the printing and typesetting industry.</p></div>
  <div class="social"><i></i><i></i><i></i><i></i></div>
  <div class="foot-brand"><b></b>BLUVEND MARKET</div>
  <div class="copy">2014 Bluvend Market.com. - All Rights Reserved</div>
</footer>

</body>
</html>
```